依頼詳細
おしゃれなイメージを希望しています。

掲載してもらいたい内容を載せています
宜しくお願いします。
①24時間営業
②11/6新規オープン(予定です。後日決定します)
③アクセスマップ(新しくできた『ふわりGATE』というモール内にコインランドリーが開店するということがわかるように)国道217号沿いでハナマルマートがあります。
④店内写真、屋外写真
⑤12/14まで全機種半額
洗濯乾燥8kg 900円→400円
洗濯乾燥15kg 1200円→600円
洗濯乾燥22kg 1500円→700円
洗濯のみ15kg 600円→300円
洗濯のみ22kg 900円→400円
洗濯のみ32kg 1100円→500円
乾燥のみ14kg 100円/10分→100円/20分
乾燥のみ25kg 100円/8分→100円/16分
シューズ用洗濯機 200円→100円
⑤洗濯機から乾燥機に移す面倒な手間いらずの全自動洗濯乾燥機を導入
⑥ふとんクリーニング店プロデュースなので羽毛布団、こたつ布団、毛布の洗濯も安心
⑦天然由来成分とEM(人体にも環境にもやさしい善玉菌の集合体)を配合した洗剤を使用しています。
記載項目
店名ロゴ(添付)、住所(大分市北松原215-3ふわりGATE C-204)、地図、店舗写真、店内写真
サイズ
A5
ページ数
両面
希望イメージ
シンプル 複雑
単色 カラフル
暗い 明るい
日常 高級
遊び心 厳粛
未来的 伝統的
女性的 男性的
希望する色
設定なし
納品ファイル
• イラストレーター形式 (.ai)
補足説明
店舗写真、店内写真は添付写真を当て込んでください。正式な写真は後日差し替えをお願いします。
新規のモール内の店舗ですので地図は大きめに表記をお願いします。
納品はアウトライン化したものとしていないものの両方お願いします。イラストレーターCS2で開けるようにしてください

訴求したい内容が一目でわかりやすい提案だったから

このたびはお忙しい中、多数のご提案をいただきありがとうございました。
今後も依頼していきますので機会がありましたらご提案くださいますようお願いします。
今後ともよろしくお願いします。

```html
<!DOCTYPE html>
<html lang="ja">
<head>
<meta charset="utf-8">
<title>Hanon Laundry</title>
<link rel="stylesheet" href="https://fonts.googleapis.com/css2?family=M+PLUS+Rounded+1c:wght@500;800&family=Noto+Sans+JP:wght@400;700;900&display=swap">
<style>
:root{
  --pink:#e8478a;
  --pink-deep:#d62c74;
  --pink-soft:#f7c9dc;
  --pink-pale:#fdeef4;
  --ink:#3a3a3a;
  --grey:#6f6f6f;
  --white:#ffffff;
}
*{margin:0;padding:0;box-sizing:border-box}
html,body{width:847px;height:1200px;overflow:hidden;background:var(--white)}
body{font-family:"Noto Sans JP",sans-serif;color:var(--ink);position:relative}
.sheet{position:absolute;inset:0;background:
  radial-gradient(ellipse at 10% 20%,#f6b7d0 0,transparent 40%),
  radial-gradient(ellipse at 90% 15%,#f3a9c7 0,transparent 38%),
  radial-gradient(ellipse at 50% 60%,#fbe0ea 0,transparent 60%),
  var(--pink-pale)}
.photos{position:absolute;top:0;left:0;right:0;height:215px;display:flex;gap:14px;padding:0 0 0 0}
.photo{flex:1;position:relative}
.photo .fill{height:175px;background:linear-gradient(#8fa9c9,#c9d3dc 55%,#9ea2a6)}
.photo:nth-child(2) .fill,.photo:nth-child(3) .fill{background:linear-gradient(#eef0f2,#d4d7da 60%,#b9bcc0)}
.caption{position:absolute;left:50%;bottom:4px;transform:translateX(-50%);white-space:nowrap;
  background:var(--white);color:var(--pink);font:800 14px "M PLUS Rounded 1c",sans-serif;
  padding:6px 16px;border-radius:20px;box-shadow:0 2px 4px rgba(0,0,0,.12)}
.points{position:absolute;top:255px;left:40px;right:40px}
.deco{position:absolute;top:0;height:50px;width:130px;background:linear-gradient(90deg,#f4b5cd,#fbd9e6)}
.deco.left{left:20px}.deco.right{right:20px}
.points h2{text-align:center;font:800 28px "M PLUS Rounded 1c",sans-serif;color:var(--ink);margin-top:60px;letter-spacing:2px}
.points h2 em{font-style:normal;color:var(--pink);font-size:34px}
.point-list{list-style:none;margin:22px 0 0 30px}
.point-list li{display:flex;gap:12px;font-size:17px;font-weight:700;line-height:1.45;margin-bottom:12px}
.point-list .num{font:900 30px "Noto Sans JP",sans-serif;color:var(--pink);font-style:italic;line-height:1}
.prices{position:absolute;top:560px;left:40px;right:40px;height:285px;background:var(--white);border:2px solid var(--pink-soft);border-radius:6px;padding:0 14px}
.prices h2{margin:12px auto 0;width:440px;background:var(--pink);color:var(--white);text-align:center;border-radius:4px;
  font:700 20px "Noto Sans JP",sans-serif;padding:4px 0}
.prices h2 b{font-size:18px;margin-left:10px}
.cols{display:flex;gap:14px;margin-top:14px}
.col{flex:1}
.col h3{background:var(--pink);color:var(--white);text-align:center;font-size:18px;padding:4px 0;border-radius:3px}
.row{display:flex;align-items:center;border-bottom:1px solid var(--pink-soft);height:54px;gap:4px}
.kg{background:var(--pink);color:var(--white);font-weight:700;font-size:14px;width:48px;text-align:center;padding:6px 0;border-radius:2px}
.old{font-size:10px;color:var(--grey);text-align:center;width:62px;line-height:1.3}
.old s{font-size:13px}
.arrow{color:var(--pink);font-size:14px}
.new{color:var(--pink-deep);font-weight:900;font-size:26px}
.new.small{font-size:16px;line-height:1.1}
.shop{position:absolute;top:870px;left:40px;width:340px}
.brand{display:flex;align-items:center;gap:8px;font:700 26px "Noto Sans JP",sans-serif;color:var(--pink)}
.brand i{width:18px;height:18px;background:var(--pink);border-radius:50%}
.addr{margin-top:8px;font-size:16px;font-weight:700;line-height:1.45}
.tel{display:flex;align-items:center;gap:6px;font-size:26px;font-weight:900;margin-top:2px}
.hours{position:absolute;top:0;right:0;width:62px;height:62px;border-radius:50%;background:var(--pink);color:var(--white);
  font-weight:900;font-size:14px;text-align:center;padding-top:13px;line-height:1.3}
.building{margin-top:10px;height:145px;background:linear-gradient(#e5e7ea,#c2c6cb)}
.map{position:absolute;top:870px;left:400px;right:40px;height:290px;background:linear-gradient(#fdf3f7,#f7d3e2);border:1px solid var(--pink-soft)}
</style>
</head>
<body>
<div class="sheet"></div>

<section class="photos">
  <figure class="photo"><div class="fill" role="img" aria-label="店舗の外観写真"></div><figcaption class="caption">店内はいつもきれいです♪</figcaption></figure>
  <figure class="photo"><div class="fill" role="img" aria-label="洗濯乾燥機が並ぶ店内写真"></div><figcaption class="caption">豊富な台数をご用意しております!</figcaption></figure>
  <figure class="photo"><div class="fill" role="img" aria-label="広い店内の写真"></div><figcaption class="caption">広いので、荷物が多くても安心!</figcaption></figure>
</section>

<section class="points">
  <div class="deco left" role="img" aria-label="物干しに干された洗濯物のイラスト"></div>
  <div class="deco right" role="img" aria-label="物干しに干された洗濯物のイラスト"></div>
  <h2>当店の<em>3</em>つのこだわりポイント</h2>
  <ol class="point-list">
    <li><span class="num">1.</span><span>洗濯機から乾燥機に移す面倒な手間いらずの全自動洗濯乾燥機を導入。</span></li>
    <li><span class="num">2.</span><span>ふとんクリーニング店プロデュースなので羽毛布団、こたつ布団、毛布の洗濯も安心。</span></li>
    <li><span class="num">3.</span><span>天然由来成分とEM(人体にも環境にもやさしい善玉菌の集合体)を配合した洗剤を使用。</span></li>
  </ol>
</section>

<section class="prices">
  <h2>料金のご案内<b>12/14(火)まで全機種半額!</b></h2>
  <div class="cols">
    <div class="col">
      <h3>洗濯乾燥</h3>
      <div class="row"><span class="kg">8kg</span><span class="old">通常価格<br><s>900円</s></span><span class="arrow">▶</span><span class="new">400円</span></div>
      <div class="row"><span class="kg">15kg</span><span class="old">通常価格<br><s>1200円</s></span><span class="arrow">▶</span><span class="new">600円</span></div>
      <div class="row"><span class="kg">22kg</span><span class="old">通常価格<br><s>1500円</s></span><span class="arrow">▶</span><span class="new">700円</span></div>
    </div>
    <div class="col">
      <h3>洗濯のみ</h3>
      <div class="row"><span class="kg">15kg</span><span class="old">通常価格<br><s>600円</s></span><span class="arrow">▶</span><span class="new">300円</span></div>
      <div class="row"><span class="kg">22kg</span><span class="old">通常価格<br><s>900円</s></span><span class="arrow">▶</span><span class="new">400円</span></div>
      <div class="row"><span class="kg">32kg</span><span class="old">通常価格<br><s>1100円</s></span><span class="arrow">▶</span><span class="new">500円</span></div>
    </div>
    <div class="col">
      <h3>乾燥のみ</h3>
      <div class="row"><span class="kg">14kg</span><span class="old">通常価格<br><s>100円/10分</s></span><span class="arrow">▶</span><span class="new small">100円/<br>20分</span></div>
      <div class="row"><span class="kg">25kg</span><span class="old">通常価格<br><s>100円/8分</s></span><span class="arrow">▶</span><span class="new small">100円/<br>16分</span></div>
      <div class="row"><span class="kg" style="font-size:10px">シューズ用<br>洗濯機</span><span class="old">通常価格<br><s>200円</s></span><span class="arrow">▶</span><span class="new">100円</span></div>
    </div>
  </div>
</section>

<section class="shop">
  <div class="brand"><i></i>Hanon Laundry</div>
  <p class="addr">大分市北松原215-3<br>ふわりGATE C-204</p>
  <p class="tel">
    <svg width="22" height="22" viewBox="0 0 24 24"><path fill="#e8478a" d="M6.6 10.8a15 15 0 0 0 6.6 6.6l2.2-2.2a1 1 0 0 1 1-.25 11.4 11.4 0 0 0 3.6.57 1 1 0 0 1 1 1V20a1 1 0 0 1-1 1A17 17 0 0 1 3 4a1 1 0 0 1 1-1h3.5a1 1 0 0 1 1 1c0 1.25.2 2.45.57 3.57a1 1 0 0 1-.25 1z"/></svg>
    0000-000-000
  </p>
  <div class="hours">24時間<br>営業</div>
  <div class="building" role="img" aria-label="ふわりGATE内の店舗位置を示す建物のイラスト"></div>
</section>

<div class="map" role="img" aria-label="国道217号沿い、ハナマルマート近くのふわりGATEへのアクセスマップ"></div>
</body>
</html>
```